Meridian Prestige Academy needs a Courses Fine Brochure

An unique business school 100% focused on the luxury market that offers programs in NY, L.A., Miami, Paris, Milan, and São Paulo, needs a comprehensive brochure with all your programs.
In two versions, to print and as a web flipping book.
Please find attached two examples of our single program brochures.
PLEASE NOTE THAT ALL UPLOADED MATERIALS ARE SAMPLES OF WHAT WE ALREADY DID, AS SOON AS I´VE CHOSEN A DESIGNER I´LL SEND THE CORRECT FILES, TEXTS AND "SUGGESTED IMAGES".
Updates

Target Market(s)

US students interested in short term programs focused on luxury.
The brochure must display 12 short term programs that will take place in 2017 in Miami, Florida.

Industry/Entity Type

Education

Contact Information for Business Card

Black sober fine finishing business card.
Name, place, phone, address, e-mail, cel.

Font styles to use
Serif
Sans Serif
Script

Requirements
Must have
• Fine finishing, as smooth touch mate lamination, and/or hotstamping, and/or located varnish.
• Easy to read. Every program has Name, brief introduction, date, time, duration, some keynote speaker picture and brief resumé (short cv). And 5 to 10 content topics. Course highlights.
Nice to have
• Luxury products and services. Sofisticated images, closeups and nice views.
• We are talking about teaching luxury for entrepreneurs mainly.
• Business owners or high level executives.
Should not have
• Less is more. Promotional look. Cheap look. Colorful blasting design.

```html
<!DOCTYPE html>
<html lang="en">
<head>
<meta charset="utf-8">
<title>Meridian Prestige Academy – Brochure Cover Spread</title>
<link rel="stylesheet" href="https://fonts.googleapis.com/css2?family=Roboto+Condensed:wght@400;700&display=swap">
<style>
  :root {
    --backdrop: #a7a7a7;
    --violet-light: #4b2c93;
    --violet: #35207a;
    --violet-deep: #1d1150;
    --gold: #d9c48f;
    --gold-pale: #efe3bd;
    --ink-light: #ffffff;
    --photo-ceiling: #e8e6f0;
    --photo-wall: #c9c5da;
    --photo-mid: #7d7894;
    --photo-floor: #3b3447;
    --photo-rug: #6b4a44;
  }
  * { box-sizing: border-box; margin: 0; padding: 0; }
  html, body {
    width: 1200px; height: 900px; overflow: hidden;
    background: var(--backdrop);
    font-family: "Roboto Condensed", "Arial Narrow", sans-serif;
  }
  .spread {
    position: absolute; left: 120px; top: 285px;
    width: 960px; height: 330px;
    display: flex;
    box-shadow: 0 10px 24px rgba(0,0,0,.28);
  }
  .page {
    position: relative; width: 480px; height: 330px; overflow: hidden;
    background: linear-gradient(160deg, var(--violet-light) 0%, var(--violet) 45%, var(--violet-deep) 100%);
  }
  .page--back { box-shadow: inset -18px 0 22px -14px rgba(0,0,0,.45); }
  .page--front { box-shadow: inset 18px 0 22px -14px rgba(0,0,0,.35); }

  .swoosh { position: absolute; inset: 0; width: 100%; height: 100%; }

  .back-contact {
    position: absolute; left: 22px; bottom: 26px; right: 22px;
    display: flex; align-items: center; gap: 16px;
  }
  .back-brand {
    display: flex; flex-direction: column; align-items: center; gap: 5px;
    width: 74px;
  }
  .brand-mark { display: block; background: var(--gold); }
  .back-brand .brand-mark { width: 26px; height: 26px; border-radius: 50%; }
  .back-brand .brand-name {
    color: var(--gold); font-weight: 700; font-size: 10px; line-height: 1.1;
    text-transform: uppercase; letter-spacing: .4px; text-align: center;
  }
  .contact-lines { color: var(--ink-light); text-align: center; flex: 1; }
  .contact-lines .school {
    font-weight: 700; font-size: 18px; text-transform: uppercase; letter-spacing: .6px;
  }
  .contact-lines .tagline,
  .contact-lines .details,
  .contact-lines .web {
    font-weight: 700; font-size: 11px; text-transform: uppercase; letter-spacing: .5px;
    margin-top: 2px;
  }
  .contact-lines .divider { margin: 0 10px; }

  .cover-photo {
    position: absolute; left: 0; top: 0; width: 100%; height: 220px;
    background:
      linear-gradient(200deg, rgba(255,255,255,.35) 0%, rgba(255,255,255,0) 40%),
      linear-gradient(180deg, var(--photo-ceiling) 0%, var(--photo-wall) 28%, var(--photo-mid) 48%, var(--photo-floor) 68%, var(--photo-rug) 100%);
  }
  .cover-wave { position: absolute; inset: 0; width: 100%; height: 100%; }
  .front-brand {
    position: absolute; right: 26px; bottom: 26px;
    display: flex; flex-direction: column; align-items: center; gap: 8px;
  }
  .front-brand .brand-mark { width: 48px; height: 48px; border-radius: 50%; }
  .front-brand .brand-name {
    color: var(--gold); font-weight: 700; font-size: 14px;
    text-transform: uppercase; letter-spacing: .6px; white-space: nowrap;
  }
</style>
</head>
<body>
  <main class="spread">
    <section class="page page--back" aria-label="Back cover">
      <svg class="swoosh" viewBox="0 0 480 330" aria-hidden="true">
        <path d="M-10 128 C 90 120, 170 90, 250 40 S 360 5, 490 8" fill="none" stroke="var(--gold)" stroke-width="3"/>
        <path d="M-10 138 C 100 132, 185 102, 262 55 S 370 20, 490 22" fill="none" stroke="var(--gold-pale)" stroke-width="1.2" opacity=".8"/>
      </svg>
      <div class="back-contact">
        <div class="back-brand">
          <span class="brand-mark" aria-hidden="true"></span>
          <span class="brand-name">Meridian Prestige Academy</span>
        </div>
        <div class="contact-lines">
          <p class="school">Meridian Prestige Academy</p>
          <p class="tagline">Excellent graduation and master degree</p>
          <p class="details">+1 305 555 0147<span class="divider">|</span>info@meridianprestige.edu</p>
          <p class="web">www.meridianprestige.edu</p>
        </div>
      </div>
    </section>

    <section class="page page--front" aria-label="Front cover">
      <div class="cover-photo" role="img" aria-label="Photograph of an elegant modern lounge interior with a faceted white ceiling, soft lighting, reflective dark floor and warm rugs"></div>
      <svg class="cover-wave" viewBox="0 0 480 330" preserveAspectRatio="none" aria-hidden="true">
        <defs>
          <linearGradient id="wave-fill" x1="0" y1="0" x2="0" y2="1">
            <stop offset="0" stop-color="var(--violet-light)"/>
            <stop offset="1" stop-color="var(--violet-deep)"/>
          </linearGradient>
        </defs>
        <path d="M0 205 C 60 165, 130 175, 200 205 S 360 195, 480 170 L480 330 L0 330 Z" fill="url(#wave-fill)"/>
        <path d="M0 198 C 60 158, 130 168, 200 198 S 360 188, 480 163" fill="none" stroke="var(--gold)" stroke-width="3"/>
        <path d="M0 210 C 65 172, 135 182, 205 210 S 362 200, 480 178" fill="none" stroke="var(--gold-pale)" stroke-width="1.2" opacity=".85"/>
      </svg>
      <div class="front-brand">
        <span class="brand-mark" aria-hidden="true"></span>
        <span class="brand-name">Meridian Prestige Academy</span>
      </div>
    </section>
  </main>
</body>
</html>
```